Custom WP Theme Build from Existing Website

Hello All,

I need a custom WP Theme and matching Logo Design built to rebrand this website:
http://tangowren.ca (current logo is top left)

We will need the new WP theme and NEW Logo Design to work well with each other.

The current logo is of a Fox sniffing out flavors. Please use your creativity to come up with a new idea that incorporates the fox. Logo must blend perfectly with WP Theme and be in the same color palette.

The look of the website must be within these subject matters
- MODERN DESIGN most important
- FUN INTERACTIVE
- COLORFUL with Carribean Flare (Think food from Carribean)
- FAST LOADING
- FULL PAGE width header (Not boxed)
- HTML5 compliant (for mobile phone)

I also need the following items for the website'

- shipping cost calculator
- promotional code option (to work with shopping cart)
- shopping cart set up to sell Hot Sauce that you see on the current website.

The shopping cart can be a script, but must allow us to build and price our inventory with ease from within the Word Press admin area. (Maybe a plugin?) Tendrix would most likely be the best payment solution, but having more options is better.

Happy bidding!

```html
<!DOCTYPE html>
<html lang="en">
<head>
<meta charset="utf-8">
<title>Tangowren – Hot Sauce Shop</title>
<link href="https://fonts.googleapis.com/css2?family=Lato:wght@300;400;700;900&family=Dancing+Script:wght@700&display=swap" rel="stylesheet">
<style>
:root{
  --blue:#1a7ef0;
  --ink:#333;
  --muted:#777;
  --line:#e4e4e4;
  --white:#fff;
  --accent:#e8501e;
}
*{box-sizing:border-box;margin:0;padding:0}
html,body{width:699px;height:1200px;overflow:hidden}
body{position:relative;font-family:'Lato',sans-serif;color:var(--ink);
  background:linear-gradient(180deg,#2f6fb8 0%,#6aa6de 14%,#3d8fc7 16%,#e7dccb 19%,#2f6fb8 20%,#6aa6de 34%,#3d8fc7 36%,#e7dccb 40%,#2f6fb8 41%,#6aa6de 55%,#3d8fc7 58%,#e7dccb 60%,#2f6fb8 61%,#6aa6de 76%,#3d8fc7 79%,#e7dccb 81%,#2f6fb8 82%,#6aa6de 96%,#e7dccb 100%)}
.abs{position:absolute}
.page{position:absolute;left:34px;top:0;width:635px;height:1200px;background:var(--white)}
.topbar{left:0;top:0;width:635px;height:19px;background:var(--blue);color:#fff;font-size:7px;display:flex;align-items:center;padding:0 25px}
.topbar .links{margin-left:auto;display:flex;gap:12px}
.header{left:0;top:19px;width:635px;height:67px;border-bottom:1px solid #eee}
.brand{font-size:17px;font-weight:400;color:var(--accent);display:flex;align-items:center;gap:5px}
.brand .dot{width:9px;height:9px;background:var(--accent);border-radius:50%}
.nav{display:flex;gap:11px;font-size:7px;color:var(--muted);align-items:center;letter-spacing:.2px}
.cartbox{width:16px;height:16px;border:1.5px solid var(--blue);color:var(--blue);font-size:7px;display:flex;align-items:center;justify-content:center;font-weight:700}
.hero{left:0;top:97px;width:635px;height:334px;background:linear-gradient(110deg,#4f7fb8 0%,#d9d1c4 25%,#e5ddd0 55%,#cfc6b6 75%,#5b88c0 100%)}
.hero-bottle{left:90px;top:0;width:100px;height:310px;background:linear-gradient(180deg,#f2efe9 0%,#c7402a 30%,#4f8a2c 60%,#b2311f 100%);border-radius:40px 40px 20px 20px}
.promo{left:318px;top:92px;width:240px;height:150px;background:rgba(210,205,230,.45);text-align:center;color:#fff}
.promo .kicker{font-family:'Dancing Script',cursive;font-size:18px;margin-top:8px}
.promo h1{font-size:30px;font-weight:900;line-height:32px;margin-top:6px}
.promo h1 span{font-size:26px;font-weight:700}
.btn{display:inline-block;margin-top:12px;background:var(--blue);color:#fff;font-size:8px;padding:6px 12px}
.tile{top:454px;width:184px;height:90px;color:#fff;font-weight:900;font-size:13px;line-height:13px;display:flex;align-items:center;justify-content:center;text-align:center}
.section-title{left:25px;width:585px;display:flex;align-items:center;gap:14px;font-size:11.5px;color:#444;text-transform:uppercase}
.section-title::before,.section-title::after{content:"";flex:1;height:1px;background:var(--line)}
.product{top:590px;height:136px}
.product-info{top:733px;text-align:center;font-size:8px;color:#555;line-height:12px}
.product-info .price{font-weight:700;color:#333}
.feature{top:820px;width:185px;text-align:center}
.feature .icon{width:26px;height:26px;margin:0 auto}
.feature h3{font-size:10px;color:#333;margin-top:12px;text-transform:uppercase;font-weight:400}
.feature p{font-size:8px;color:#777;line-height:14px;margin-top:20px}
.totop{left:632px;top:941px;width:23px;height:22px;background:#111}
.testimonials{left:0;top:969px;width:635px;height:167px;background:linear-gradient(90deg,#3a2c27 0%,#4a3a33 55%,#a99d92 78%,#6e615a 100%)}
.quote-box{left:71px;top:41px;width:452px;height:89px;background:rgba(255,255,255,.06)}
.avatar{left:29px;top:11px;width:44px;height:44px;border-radius:50%;background:#a89485;border:2px solid #ddd}
.quote{left:95px;top:23px;width:360px;font-size:8px;font-style:italic;color:#ddd;line-height:11px}
.footer{left:0;top:1153px;width:635px;height:47px;background:var(--blue);color:rgba(255,255,255,.75);font-size:6.5px;padding:11px 26px}
.footer .links{display:flex;gap:9px}
</style>
</head>
<body>
<div class="page">
  <div class="abs topbar"><span>Add anything here here or just remove it...</span>
    <div class="links"><span>Blog</span><span>About us</span><span>Contact us</span><span>FAQ</span><span>My Account</span><span>Logout</span></div></div>

  <div class="abs header">
    <div class="abs brand" style="left:32px;top:24px">Tangowren<span class="dot"></span></div>
    <div class="abs nav" style="left:162px;top:30px">
      <svg width="8" height="8" viewBox="0 0 10 10"><circle cx="4" cy="4" r="3" fill="none" stroke="#777" stroke-width="1.3"/><line x1="6.3" y1="6.3" x2="9" y2="9" stroke="#777" stroke-width="1.3"/></svg>
      <span>HOME</span><span>ABOUT US</span><span>SHOP</span><span>OUR SERVICES</span><span>CONTACT US</span></div>
    <div class="abs nav" style="left:475px;top:23px"><span>MY ACCOUNT</span><span style="margin-left:12px">CART / £0</span><span class="cartbox">0</span></div>
  </div>

  <div class="abs hero">
    <div class="abs hero-bottle" role="img" aria-label="Photo of a hand holding a bottle of hot sauce in front of an apron"></div>
    <div class="abs promo">
      <div class="kicker">This Weekend Only</div>
      <h1>FREE SHIPPING<br><span>ON ALL ORDERS!</span></h1>
      <span class="btn">BROWSE PRODUCTS</span>
    </div>
    <svg class="abs" style="left:14px;top:151px" width="22" height="22"><circle cx="11" cy="11" r="10" fill="none" stroke="#333" stroke-width="1.5"/><polyline points="13,6 8,11 13,16" fill="none" stroke="#333" stroke-width="1.5"/></svg>
    <svg class="abs" style="left:599px;top:151px" width="22" height="22"><circle cx="11" cy="11" r="10" fill="none" stroke="#333" stroke-width="1.5"/><polyline points="9,6 14,11 9,16" fill="none" stroke="#333" stroke-width="1.5"/></svg>
    <svg class="abs" style="left:307px;top:308px" width="20" height="8"><circle cx="4" cy="4" r="3" fill="none" stroke="#333"/><circle cx="13" cy="4" r="3.3" fill="#111"/></svg>
  </div>

  <div class="abs tile" style="left:25px;background:linear-gradient(135deg,#ecebe6,#d6d3c9)" role="img" aria-label="Photo of fresh vegetables and spices on a white table">WEEKLY<br>GIVEAWAY</div>
  <div class="abs tile" style="left:225px;background:linear-gradient(135deg,#8a8580,#5c5650)" role="img" aria-label="Photo of a bulldog looking at the camera">JOIN OUR<br>COMPETITION</div>
  <div class="abs tile" style="left:426px;background:linear-gradient(135deg,#eeeae6,#c9a7a7)" role="img" aria-label="Photo of a beetroot with leaves">ABOUT US</div>

  <div class="abs section-title" style="top:560px">Weekly Featured Products</div>
  <div class="abs product" style="left:28px;width:124px;background:linear-gradient(180deg,#f4f4f4 0%,#c8452c 35%,#6a9a34 70%,#b4361f 100%)" role="img" aria-label="Three bottles of red hot sauce"></div>
  <div class="abs product" style="left:176px;width:128px;background:linear-gradient(180deg,#f4f4f4 0%,#e58c55 35%,#7aa23c 70%,#dd7d44 100%)" role="img" aria-label="Three bottles of orange hot sauce"></div>
  <div class="abs product" style="left:323px;width:136px;background:linear-gradient(180deg,#222 0%,#c5772f 35%,#5f8a2e 70%,#b8682a 100%)" role="img" aria-label="Three jars of brown barbecue sauce"></div>
  <div class="abs product" style="left:479px;width:132px;background:linear-gradient(180deg,#f4f4f4 0%,#c84a2d 35%,#6a9a34 70%,#b4381f 100%)" role="img" aria-label="Three bottles of red hot sauce"></div>

  <div class="abs product-info" style="left:28px;width:124px">Classic Hot Sauce<br><span class="price">£6.00</span></div>
  <div class="abs product-info" style="left:176px;width:128px">Mango Hot Sauce<br><span class="price">£6.00</span></div>
  <div class="abs product-info" style="left:323px;width:136px">Jerk BBQ Sauce<br><span class="price">£7.00</span></div>
  <div class="abs product-info" style="left:479px;width:132px">Extra Hot Sauce<br><span class="price">£6.50</span></div>

  <div class="abs section-title" style="top:788px">Amazing Features</div>
  <div class="abs feature" style="left:25px">
    <svg class="icon" viewBox="0 0 26 26"><circle cx="13" cy="13" r="12" fill="none" stroke="#ccc" stroke-width="1.3"/><polygon points="13,7 14.8,11 19,11.3 15.8,14 16.8,18.2 13,16 9.2,18.2 10.2,14 7,11.3 11.2,11" fill="#ccc"/></svg>
    <h3>Free Shipping on all ordres</h3>
    <p>Get Free Shipping on all orders over $75 and free returns to our UK returns centre! Items are dispatched from the US and will arrive in 5-8 days.</p></div>
  <div class="abs feature" style="left:225px">
    <svg class="icon" viewBox="0 0 26 26"><circle cx="13" cy="13" r="12" fill="none" stroke="#ccc" stroke-width="1.3"/><path d="M13 18 C8 14 8 9.5 10.5 9.5 C12 9.5 13 11 13 11 C13 11 14 9.5 15.5 9.5 C18 9.5 18 14 13 18Z" fill="#ccc"/></svg>
    <h3>Amazing customer service</h3>
    <p>Get Free Shipping on all orders over $75 and free returns to our UK returns centre! Items are dispatched from the US and will arrive in 5-8 days.</p></div>
  <div class="abs feature" style="left:425px">
    <svg class="icon" viewBox="0 0 26 26"><circle cx="13" cy="13" r="12" fill="none" stroke="#ccc" stroke-width="1.3"/><path d="M10 18 L10 10 M12.5 18 L12.5 8 M15 18 L15 9 M17 17 L17 12" stroke="#ccc" stroke-width="1.6" stroke-linecap="round"/></svg>
    <h3>No customs or duty fees!</h3>
    <p>We pay these fees so you don't have to! The total billed at checkout is the final amount you pay, inclusive of VAT, with no additional charges at the time of delivery!</p></div>

  <div class="abs totop"><svg width="23" height="22"><polyline points="7,13 11.5,8.5 16,13" fill="none" stroke="#fff" stroke-width="1.6"/></svg></div>

  <div class="abs testimonials" role="img" aria-label="Photo of a smiling young woman on a dark background">
    <div class="abs quote-box">
      <div class="abs avatar" role="img" aria-label="Customer portrait"></div>
      <svg class="abs" style="left:96px;top:8px" width="48" height="9" viewBox="0 0 48 9">
        <g fill="#d99a3c"><polygon points="4.5,0 5.8,3 9,3.3 6.6,5.3 7.4,8.6 4.5,6.8 1.6,8.6 2.4,5.3 0,3.3 3.2,3"/><polygon transform="translate(9.5 0)" points="4.5,0 5.8,3 9,3.3 6.6,5.3 7.4,8.6 4.5,6.8 1.6,8.6 2.4,5.3 0,3.3 3.2,3"/><polygon transform="translate(19 0)" points="4.5,0 5.8,3 9,3.3 6.6,5.3 7.4,8.6 4.5,6.8 1.6,8.6 2.4,5.3 0,3.3 3.2,3"/></g>
        <g fill="none" stroke="#d99a3c" stroke-width=".7"><polygon transform="translate(28.5 0)" points="4.5,0 5.8,3 9,3.3 6.6,5.3 7.4,8.6 4.5,6.8 1.6,8.6 2.4,5.3 0,3.3 3.2,3"/><polygon transform="translate(38 0)" points="4.5,0 5.8,3 9,3.3 6.6,5.3 7.4,8.6 4.5,6.8 1.6,8.6 2.4,5.3 0,3.3 3.2,3"/></g></svg>
      <p class="abs quote">PBR kogi VHS commodo, single-origin coffee selvage kale chips. Fugiat try-hard ad aesthetic, tofu master cleanse typewriter tote bag accusamus sustainable ennui hella small batch cliche.</p>
      <div class="abs" style="left:96px;top:57px;width:17px;height:1px;background:#888"></div>
      <div class="abs" style="left:96px;top:64px;font-size:8px;font-style:italic;font-weight:700;color:#eee">Mara Ellison <span style="font-weight:400;color:#998">Chirpnet</span></div>
    </div>
    <svg class="abs" style="left:303px;top:141px" width="30" height="8"><circle cx="4" cy="4" r="3.3" fill="#fff"/><circle cx="13" cy="4" r="3" fill="none" stroke="#ccc"/><circle cx="22" cy="4" r="3" fill="none" stroke="#ccc"/></svg>
  </div>

  <div class="abs footer">
    <div class="links"><span>BLOG</span><span>ABOUT US</span><span>CONTACT US</span><span>FAQ</span><span>MY ACCOUNT</span><span>LOGOUT</span></div>
    <div style="margin-top:10px;font-size:7px">Copyright 2014 © BRIGHTLANE.CO.</div>
  </div>
</div>
</body>
</html>
```